Ninety Truths Gathered Across Four Decades Advising Firms

I need the design for my book cover, plus the spine and the back cover. I need this for both a hard cover book and an ebook

Target Market(s)

Any person in business with managerial responsibility

Industry/Entity Type

Consulting

Font styles to use
Serif

Requirements
Must have
• Must look very professional. No script/cursive is to be used. The cover should be clean, not cluttered.so the title really stands out well
Nice to have
• A professional image to reinforce the title
Should not have
• Script, cartoons or anything that does not look professional

```html
<!DOCTYPE html>
<html lang="en">
<head>
<meta charset="utf-8">
<title>Ninety Truths Gathered Across Four Decades Advising Firms — Spine and Front Cover</title>
<link rel="stylesheet" href="https://fonts.googleapis.com/css2?family=Anton&family=Roboto+Condensed:wght@300;400;700&display=swap">
<style>
  :root {
    --backdrop: #d9d9d9;
    --cover: #ffffff;
    --spine: #f4f4f4;
    --maroon: #5c1722;
    --author-grey: #6e6e6e;
    --table-light: #d4d4d4;
    --table-dark: #8a8a8a;
  }
  * { margin: 0; padding: 0; box-sizing: border-box; }
  html, body {
    width: 1200px;
    height: 800px;
    overflow: hidden;
    background: var(--backdrop);
    -webkit-font-smoothing: antialiased;
    -moz-osx-font-smoothing: grayscale;
    text-rendering: geometricPrecision;
  }
  .canvas {
    width: 1200px;
    height: 800px;
    display: flex;
    align-items: center;
    justify-content: center;
  }
  .book {
    display: flex;
    box-shadow: 0 2px 10px rgba(0,0,0,0.12);
  }
  .spine {
    width: 60px;
    height: 720px;
    background: var(--spine);
    border-right: 1px solid #e2e2e2;
    display: flex;
    align-items: center;
    justify-content: center;
  }
  .spine-text {
    writing-mode: vertical-rl;
    white-space: nowrap;
    font-family: "Roboto Condensed", "Arial Narrow", sans-serif;
    text-transform: uppercase;
    display: flex;
    align-items: center;
    gap: 22px;
  }
  .spine-title {
    font-weight: 700;
    font-size: 17px;
    color: var(--maroon);
  }
  .spine-author {
    font-weight: 400;
    font-size: 17px;
    letter-spacing: 1px;
    color: var(--author-grey);
  }
  .front-cover {
    position: relative;
    width: 480px;
    height: 720px;
    background: var(--cover);
  }
  .title {
    position: absolute;
    top: 92px;
    left: 0;
    width: 100%;
    text-align: center;
    color: var(--maroon);
    text-transform: uppercase;
    font-weight: 400;
    line-height: 0.92;
  }
  .title span { display: block; }
  .title .line-xl,
  .title .line-lg,
  .title .line-final {
    font-family: "Anton", "Arial Narrow", sans-serif;
  }
  .title .line-xl { font-size: 66px; }
  .title .line-lg { font-size: 56px; }
  .title .line-final { font-size: 84px; letter-spacing: 1px; }
  .title .line-sm {
    font-family: "Roboto Condensed", "Arial Narrow", sans-serif;
    font-weight: 700;
    font-size: 26px;
    line-height: 1.1;
  }
  .boardroom-image {
    position: absolute;
    top: 420px;
    left: 130px;
    width: 220px;
    height: 104px;
    border-radius: 0 0 110px 110px / 0 0 104px 104px;
    background: radial-gradient(ellipse at 50% 0%, var(--table-light) 0%, #b3b3b3 55%, var(--table-dark) 100%);
    opacity: 0.9;
  }
  .author-name {
    position: absolute;
    top: 590px;
    left: 0;
    width: 100%;
    text-align: center;
    font-family: "Roboto Condensed", "Arial Narrow", sans-serif;
    font-weight: 300;
    font-size: 34px;
    letter-spacing: 4px;
    color: var(--author-grey);
    text-transform: uppercase;
  }
</style>
</head>
<body>
  <main class="canvas">
    <div class="book">
      <aside class="spine">
        <p class="spine-text">
          <span class="spine-title">Ninety Truths Gathered Across Four Decades Advising Firms</span>
          <span class="spine-author">Author’s Name</span>
        </p>
      </aside>
      <section class="front-cover">
        <h1 class="title">
          <span class="line-xl">Ninety</span>
          <span class="line-xl">Truths</span>
          <span class="line-sm">Gathered Across</span>
          <span class="line-lg">Four Decades</span>
          <span class="line-sm">Advising</span>
          <span class="line-final">Firms</span>
        </h1>
        <div class="boardroom-image" role="img" aria-label="Illustration of a curved, tiered boardroom table with rows of seated figures seen from above"></div>
        <p class="author-name">Author’s Name</p>
      </section>
    </div>
  </main>
</body>
</html>
```